GLINT GIN BY TIDE LURE CO

We plan to use a rum product from the caribbean country of Belize CA. That will need to be mentioned somewhere on the label. We want to do a more high-line product, an aged dark rum that plays on the shark theme. We want to use a sleek bottle design with a clever label. Or unique label placement. We need something that will pop off the shelf. We want you to have fun with it and see where it goes. We like the idea of sharks circling around the bottle, possibly like an etching on the glass or back printed on the label or a clear label that can feature the sharks in some capacity. (Not a must) "Chum" because it attracts sharks.

The "Glint Gin" needs a FONT that can become synonymous with the word and then the product. Glint Gin is to be the focus and Tide Lure Co is merely the parent company and requires mention.
Ex:
Tide Lure co.'s Glint Gin
produced in Belize, CA
or Glint Gin produced in Belize for
Tide Lure co.

We have a Glint Gin "mascot" or stamp that is a tribal shark drawing that we want used in the designs where ever you feel fit. We like the stamp as it is, but if you have some tweaks we may consider them.
Updates

I have increased first place to $450.00  and 2nd place to$150.00 !!!

 Everything we have gotten has been great just looking for more ideas. Looking for something sharp and sleek for our bottle we are trying to sell a  upscale rum !! We need it for a aged rum & a white rum .. 

  Thank you !! 
  Torvin

Target Market(s)

MALE 25 TO 45

Industry/Entity Type

It Company

Requirements
Must have
• SHARK THEME ...
Should not have
• OLD WORLD LOOK / MAP LOOKING / TRADITIONAL/ CHEAP.
We don't want everything that has already been done, like all the pirate themes. You can hint at any of these elements in a clever understated way. It is rum after all!

```html
<!DOCTYPE html>
<html lang="en">
<head>
<meta charset="utf-8">
<title>Glint Gin – Label</title>
<link href="https://fonts.googleapis.com/css2?family=Josefin+Sans:wght@400&family=Tinos:wght@400;700&family=Arimo:wght@400&display=swap" rel="stylesheet">
<style>
  :root {
    --bg: #ffffff;
    --cream: #fbf0d2;
    --cream-deep: #f3d99a;
    --gold: #e9b23a;
    --gold-light: #fce7a8;
    --amber: #d8961f;
    --ink: #1c1a17;
    --brown: #7d6648;
    --brown-dark: #5a4632;
    --text-cream: #f4ead2;
    --logo-gold: #f0bd45;
  }
  html, body {
    margin: 0;
    padding: 0;
    width: 1200px;
    height: 869px;
    overflow: hidden;
    background: var(--bg);
  }
  .canvas {
    position: relative;
    width: 1200px;
    height: 869px;
  }
  .main-label {
    position: absolute;
    left: 400px;
    top: 50px;
    width: 400px;
    height: 460px;
  }
  .info-label {
    position: absolute;
    left: 445px;
    top: 575px;
    width: 310px;
    height: 140px;
  }
  .serif { font-family: "Tinos", "Times New Roman", serif; }
  .sans { font-family: "Arimo", Arial, sans-serif; }
  .brand-name {
    font-family: "Josefin Sans", "Century Gothic", sans-serif;
    font-weight: 400;
    fill: var(--logo-gold);
  }
</style>
</head>
<body>
<main class="canvas">

  <svg class="main-label" viewBox="0 0 400 460" aria-label="Glint Gin front label">
    <defs>
      <linearGradient id="label-paper" x1="0" y1="0" x2="0" y2="1">
        <stop offset="0" stop-color="var(--cream)"/>
        <stop offset="1" stop-color="var(--cream-deep)"/>
      </linearGradient>
      <linearGradient id="label-band" x1="0" y1="0" x2="0" y2="1">
        <stop offset="0" stop-color="var(--gold-light)"/>
        <stop offset="0.5" stop-color="var(--gold)"/>
        <stop offset="1" stop-color="var(--amber)"/>
      </linearGradient>
      <linearGradient id="shark-tone" x1="0" y1="0" x2="1" y2="1">
        <stop offset="0" stop-color="#d9c39a"/>
        <stop offset="1" stop-color="#a58a62"/>
      </linearGradient>
      <clipPath id="label-shape">
        <path d="M22,42 Q200,12 378,42 L378,128 L346,160 L366,318 L200,452 L34,318 L54,160 L22,128 Z"/>
      </clipPath>
    </defs>

    <g class="label-body" clip-path="url(#label-shape)">
      <rect width="400" height="460" fill="url(#label-paper)"/>
      <rect class="label-band" x="0" y="200" width="400" height="80" fill="url(#label-band)"/>
    </g>
    <path class="label-edge" d="M22,42 Q200,12 378,42 L378,128 L346,160 L366,318 L200,452 L34,318 L54,160 L22,128 Z" fill="none" stroke="var(--brown)" stroke-width="1.5"/>
    <path class="label-inner-edge" d="M34,52 Q200,24 366,52 L366,124 L334,156 L354,312 L200,438 L46,312 L66,156 L34,124 Z" fill="none" stroke="var(--brown)" stroke-width="0.8" opacity="0.6"/>

    <g class="pinstripes" stroke="var(--brown)" stroke-width="0.8" opacity="0.55">
      <line x1="140" y1="72" x2="260" y2="72"/>
      <line x1="130" y1="80" x2="270" y2="80"/>
      <line x1="124" y1="88" x2="276" y2="88"/>
      <line x1="118" y1="96" x2="282" y2="96"/>
    </g>

    <rect class="top-tab" x="118" y="28" width="164" height="22" fill="var(--ink)"/>
    <text class="serif" x="200" y="44" text-anchor="middle" font-size="10.5" letter-spacing="0.6" fill="var(--text-cream)">ORIGINAL BLACK RUM</text>

    <rect class="shark-art" role="img" aria-label="Illustrated shark head with open jaws, facing right" x="38" y="66" width="100" height="112" rx="14" fill="url(#shark-tone)" opacity="0.85"/>
    <rect class="shark-art" role="img" aria-label="Illustrated shark head with open jaws, facing left" x="262" y="66" width="100" height="112" rx="14" fill="url(#shark-tone)" opacity="0.85"/>

    <polygon class="crest-frame" points="106,120 294,120 340,222 294,322 106,322 60,222" fill="none" stroke="var(--brown)" stroke-width="2"/>
    <polygon class="crest" points="114,130 286,130 328,222 286,312 114,312 72,222" fill="var(--ink)"/>

    <text class="brand-name" x="200" y="208" text-anchor="middle" font-size="50" letter-spacing="1">GLINT</text>
    <text class="brand-name" x="200" y="282" text-anchor="middle" font-size="66" letter-spacing="1">GIN</text>

    <path class="maker-bar" d="M124,300 L276,300 L268,334 L132,334 Z" fill="var(--brown)"/>
    <text class="serif" x="200" y="323" text-anchor="middle" font-size="15" letter-spacing="0.5" fill="var(--text-cream)">TIDE LURE CO</text>

    <text class="serif" x="200" y="376" text-anchor="middle" font-size="21" font-weight="700" fill="var(--ink)">BLACK</text>
    <path class="base-chevron" d="M112,392 L200,430 L288,392" fill="none" stroke="var(--brown)" stroke-width="1.2"/>
  </svg>

  <svg class="info-label" viewBox="0 0 310 140" aria-label="Glint Gin details label">
    <defs>
      <linearGradient id="info-paper" x1="0" y1="0" x2="0" y2="1">
        <stop offset="0" stop-color="var(--cream)"/>
        <stop offset="1" stop-color="var(--gold)"/>
      </linearGradient>
    </defs>
    <rect x="1" y="1" width="308" height="138" rx="10" fill="url(#info-paper)" stroke="var(--brown)" stroke-width="0.8"/>
    <text class="serif" x="155" y="30" text-anchor="middle" font-size="16" letter-spacing="0.4" fill="var(--brown-dark)">Original Premium Crafted Rum</text>
    <rect class="info-band" x="1" y="42" width="308" height="46" fill="var(--ink)"/>
    <text class="sans" x="155" y="61" text-anchor="middle" font-size="13" fill="var(--text-cream)">Tide Lure co.'s</text>
    <text class="sans" x="155" y="79" text-anchor="middle" font-size="13" fill="var(--text-cream)">Glint Gin produced in Belize, CA</text>
    <text class="serif" x="22" y="120" font-size="16" font-weight="700" fill="var(--ink)">37,5% vol</text>
    <text class="serif" x="288" y="120" text-anchor="end" font-size="16" font-weight="700" fill="var(--ink)">700ml ℮</text>
  </svg>

</main>
</body>
</html>
```